To design the Curriculum Vitae of a General Manager Legal

the objective is to redesign the attached Résumé for a senior level Internal Legal Executive in order to make it attractive, easily readable, catchy, modern looking while staying classy, elegant, sobre, and serious.
The résumé is attached to this project. it contains the followings sections : Photo; Contact Details; Summary; Education; Experience; Other.
Feel free to use photoshop to improve photo.
Updates

Target Market(s)

Legal community; law firms; Big corporations requiring internal legal senior executive

Font styles to use
Serif

Colors
ffffff
85cae6
33a6d7
0292cd
86cfc6
cfeae6
757575
919191
d9d9d9

Requirements
Must have
• classy; serious; professional; elegant; easy to read; catchy; modern;

```html
<!DOCTYPE html>
<html lang="en">
<head>
<meta charset="utf-8">
<title>Lina Haddad Mourad – Curriculum Vitae</title>
<link rel="stylesheet" href="https://fonts.googleapis.com/css2?family=Gelasio:wght@400;700&family=Jost:wght@300&display=swap">
<style>
  :root {
    --page: #ffffff;
    --accent: #0292cd;
    --rule: #cccccc;
    --ink: #1a1a1a;
    --muted: #919191;
    --photo-dark: #3a3634;
    --photo-warm: #7a5a48;
  }
  * { margin: 0; padding: 0; box-sizing: border-box; }
  html, body { width: 927px; height: 1200px; overflow: hidden; background: var(--page); }
  .cv {
    position: relative;
    width: 927px;
    height: 1200px;
    background: var(--page);
    font-family: "Gelasio", Georgia, serif;
    color: var(--ink);
  }
  .side-band {
    position: absolute;
    left: 13px; top: 13px;
    width: 31px; height: 1175px;
    background: var(--rule);
  }
  .identity { position: absolute; left: 110px; top: 78px; }
  .name {
    font-size: 25px;
    font-weight: 400;
    color: var(--accent);
    line-height: 1.2;
    letter-spacing: 0.2px;
  }
  .title { font-size: 17.5px; line-height: 1.3; margin-top: 3px; }
  .contact {
    margin-top: 17px;
    font-family: "Jost", "Helvetica Neue", sans-serif;
    font-weight: 300;
    font-size: 18px;
    color: var(--muted);
    line-height: 23px;
  }
  .contact-row { display: flex; }
  .contact-label { width: 109px; }
  .portrait {
    position: absolute;
    left: 629px; top: 61px;
    width: 197px; height: 217px;
    background: linear-gradient(160deg, var(--photo-dark) 0%, var(--photo-warm) 55%, #b89a88 100%);
  }
  .section-title {
    position: absolute;
    left: 0; right: 0; top: 364px;
    text-align: center;
    padding-left: 36px;
    font-size: 19px;
    font-weight: 700;
    color: var(--accent);
    letter-spacing: 0.3px;
  }
  .summary {
    position: absolute;
    left: 110px; top: 440px;
    width: 742px;
    font-size: 14.4px;
    line-height: 19.2px;
    text-align: justify;
  }
  .summary p + p { margin-top: 19px; }
</style>
</head>
<body>
<main class="cv">
  <div class="side-band"></div>

  <header class="identity">
    <h1 class="name">Lina Haddad Mourad</h1>
    <p class="title">Senior Level Legal Professional</p>
    <div class="contact">
      <div class="contact-row"><span class="contact-label">Mobile:</span><span>+971 50 4187260</span></div>
      <div class="contact-row"><span class="contact-label">E-mail:</span><span>lina.mourad@example.com</span></div>
    </div>
  </header>

  <div class="portrait" role="img" aria-label="Portrait photo of the legal professional"></div>

  <h2 class="section-title">SUMMARY</h2>

  <section class="summary">
    <p>I am a senior level legal professional with more than 15 years of experience in-house and in private practice, focusing on Real Estate, Retail and Services.</p>
    <p>My skills include Transactional (M&amp;A, real estate, commercial, corporate restructuring, and strategic funding), Organizational (corporate policies and procedures and authority, Legal (preemptive legal advice, and multi jurisdiction litigation management expertise), and Managerial (optimizing the value add of the legal department as both service provider and risk gatekeeper).</p>
    <p>I am currently a GM-Legal at Al Noor Holding Group, an internationally recognized industry Leader in shopping malls, communities, retail and leisure across the Middle East, Africa and Asia.&nbsp; I joined the company in November 2011 as Legal Counsel at Al Noor Properties responsible for UAE Shopping Malls, Project management and communities, and then moved in 2015 to Al Noor Retail - Marketline where I currently as GM-Legal, focus on leading and managing the group’s legal, compliance and risk management strategies in countries across a wide geographic area.</p>
    <p>Prior to moving to Dubai, I lived in Paris, France, where I worked in various organizations including the Global Chamber Court of Arbitration, as well as a billing software company and a consultancy practice.</p>
    <p>I graduated from the University of Lutèce with two Master Degrees and I am a mother of three who is passionate about Women Empowerment and Refugee Children Education.</p>
  </section>
</main>
</body>
</html>
```